MindHarbr Powerpoint Presentation Template

I am looking for a PowerPoint template that I can use for my presentations. I have attached a copy of my logo that your community has previously designed for me. My presentations are typically visual with very little text being used.
I have included my current presentation style using my old corporate colours (they are very different). There is one condition, the template must not have a white background as this detracts the focus of the crowd away from the presenter (which defeats the purpose of having a presenter in the first place).
Thank you for your time in coming up with a design!
Lorn
Look and feel
Each slider illustrates characteristics of the customer's brand and the style your logo design should communicate.

```html
<!DOCTYPE html>
<html lang="en">
<head>
<meta charset="utf-8">
<title>MindHarbr Presentation Template</title>
<link rel="stylesheet" href="https://fonts.googleapis.com/css2?family=Montserrat:wght@400;500;600;700&display=swap">
<style>
  :root {
    --page: #c5c6c8;
    --blue: #1ba8ea;
    --blue-deep: #0f86c4;
    --ink: #07090d;
    --night: #151b24;
    --navy: #10273d;
    --white: #ffffff;
  }
  * { margin: 0; padding: 0; box-sizing: border-box; }
  html, body { width: 826px; height: 1200px; overflow: hidden; }
  body {
    position: relative;
    background: var(--page);
    font-family: "Montserrat", Arial, sans-serif;
  }
  .slide { position: absolute; display: block; box-shadow: 0 1px 3px rgba(0,0,0,.15); }
  .slide text { font-family: "Montserrat", Arial, sans-serif; }
  .slide--hero { left: 171px; top: 89px; width: 484px; height: 272px; }
  .slide--title-blue { left: 35px; top: 510px; width: 372px; height: 209px; }
  .slide--title-light { left: 419px; top: 510px; width: 372px; height: 209px; }
  .slide--statement { left: 35px; top: 731px; width: 372px; height: 209px; }
  .slide--content { left: 419px; top: 731px; width: 372px; height: 209px; }
  .slide--features { left: 35px; top: 953px; width: 372px; height: 209px; }
  .slide--contact { left: 419px; top: 953px; width: 372px; height: 209px; }
  .t-blue { fill: var(--blue); }
  .t-white { fill: var(--white); }
  .t-ink { fill: var(--ink); }
  .t-navy { fill: var(--navy); }
</style>
</head>
<body>

<!-- Title slide, blue version (large) -->
<svg class="slide slide--hero" viewBox="0 0 372 209" role="group" aria-label="Title slide">
  <defs>
    <linearGradient id="photoBlue" x1="0" y1="0" x2="1" y2="1">
      <stop offset="0" stop-color="#6fb4d8"/>
      <stop offset="0.5" stop-color="#2d4e66"/>
      <stop offset="1" stop-color="#1a2630"/>
    </linearGradient>
  </defs>
  <rect width="372" height="209" fill="url(#photoBlue)" role="img" aria-label="Photo: business people shaking hands over a tablet showing a chart"/>
  <polygon points="0,0 291,0 200,209 0,209" fill="var(--blue)" opacity="0.88"/>
  <polygon points="0,103 244,209 0,209" fill="var(--ink)"/>
  <text class="t-ink" x="27" y="41" font-size="19" font-weight="600">Psychological</text>
  <text class="t-ink" x="27" y="61" font-size="19" font-weight="600">Safety</text>
  <text class="t-ink" x="27" y="79" font-size="7.6">The essential ingredient to every</text>
  <text class="t-ink" x="27" y="87.5" font-size="7.6">great workplace culture and high</text>
  <text class="t-ink" x="27" y="96" font-size="7.6">performing team.</text>
  <circle cx="112" cy="163" r="5" fill="var(--blue)"/>
  <text class="t-white" x="27" y="168" font-size="13" font-weight="700">MindHarbr</text>
  <text class="t-blue" x="27" y="175" font-size="4.2">REALISING HUMAN POTENTIAL</text>
  <rect x="238" y="201" width="134" height="8" fill="var(--ink)" opacity="0.6"/>
  <text x="366" y="206.5" font-size="3.8" text-anchor="end" class="t-white"><tspan class="t-blue" font-weight="600">Lorn Ashby</tspan> © 2021 | www.<tspan class="t-blue" font-weight="600">lornashby</tspan>.nz</text>
</svg>

<!-- Title slide, blue version -->
<svg class="slide slide--title-blue" viewBox="0 0 372 209" role="group" aria-label="Title slide">
  <rect width="372" height="209" fill="url(#photoBlue)" role="img" aria-label="Photo: business people shaking hands over a tablet showing a chart"/>
  <polygon points="0,0 291,0 200,209 0,209" fill="var(--blue)" opacity="0.88"/>
  <polygon points="0,103 244,209 0,209" fill="var(--ink)"/>
  <text class="t-ink" x="27" y="41" font-size="19" font-weight="600">Psychological</text>
  <text class="t-ink" x="27" y="61" font-size="19" font-weight="600">Safety</text>
  <text class="t-ink" x="27" y="79" font-size="7.6">The essential ingredient to every</text>
  <text class="t-ink" x="27" y="87.5" font-size="7.6">great workplace culture and high</text>
  <text class="t-ink" x="27" y="96" font-size="7.6">performing team.</text>
  <circle cx="112" cy="163" r="5" fill="var(--blue)"/>
  <text class="t-white" x="27" y="168" font-size="13" font-weight="700">MindHarbr</text>
  <text class="t-blue" x="27" y="175" font-size="4.2">REALISING HUMAN POTENTIAL</text>
  <rect x="238" y="201" width="134" height="8" fill="var(--ink)" opacity="0.6"/>
  <text x="366" y="206.5" font-size="3.8" text-anchor="end" class="t-white"><tspan class="t-blue" font-weight="600">Lorn Ashby</tspan> © 2021 | www.<tspan class="t-blue" font-weight="600">lornashby</tspan>.nz</text>
</svg>

<!-- Title slide, light corner version -->
<svg class="slide slide--title-light" viewBox="0 0 372 209" role="group" aria-label="Title slide">
  <defs>
    <linearGradient id="photoTeam" x1="0" y1="0" x2="1" y2="1">
      <stop offset="0" stop-color="#3b4653"/>
      <stop offset="0.55" stop-color="#5e7386"/>
      <stop offset="1" stop-color="#b9cfdc"/>
    </linearGradient>
  </defs>
  <rect width="372" height="209" fill="url(#photoTeam)" role="img" aria-label="Photo: smiling business team gathered around a table"/>
  <polygon points="0,0 291,0 200,209 0,209" fill="var(--ink)" opacity="0.75"/>
  <polygon points="0,103 244,209 0,209" fill="var(--white)"/>
  <text class="t-blue" x="27" y="41" font-size="19" font-weight="600">Psychological</text>
  <text class="t-blue" x="27" y="61" font-size="19" font-weight="600">Safety</text>
  <text class="t-white" x="27" y="79" font-size="7.6">The essential ingredient to every</text>
  <text class="t-white" x="27" y="87.5" font-size="7.6">great workplace culture and high</text>
  <text class="t-white" x="27" y="96" font-size="7.6">performing team.</text>
  <circle cx="112" cy="163" r="5" fill="var(--blue)"/>
  <text class="t-navy" x="27" y="168" font-size="13" font-weight="700">MindHarbr</text>
  <text class="t-navy" x="27" y="175" font-size="4.2">REALISING HUMAN POTENTIAL</text>
  <rect x="238" y="200" width="134" height="9" fill="var(--blue)"/>
  <text x="366" y="206.2" font-size="3.8" text-anchor="end" class="t-white"><tspan font-weight="700">Lorn Ashby</tspan> © 2021 | www.<tspan font-weight="700">lornashby</tspan>.nz</text>
</svg>

<!-- Statement slide -->
<svg class="slide slide--statement" viewBox="0 0 372 209" role="group" aria-label="Statement slide">
  <defs>
    <linearGradient id="photoDark" x1="0" y1="0" x2="1" y2="1">
      <stop offset="0" stop-color="#20262e"/>
      <stop offset="0.6" stop-color="#2f3a4a"/>
      <stop offset="1" stop-color="#1a1f26"/>
    </linearGradient>
  </defs>
  <rect width="372" height="209" fill="url(#photoDark)" role="img" aria-label="Dimmed photo: business handshake over a desk with a laptop"/>
  <circle cx="174" cy="70" r="4" fill="var(--blue)"/>
  <text class="t-white" x="186" y="74" font-size="11" font-weight="700" text-anchor="middle">MindHarbr</text>
  <text class="t-blue" x="186" y="80" font-size="3.6" text-anchor="middle">REALISING HUMAN POTENTIAL</text>
  <text class="t-white" x="186" y="124" font-size="9" text-anchor="middle">This is what we call</text>
  <text class="t-blue" x="186" y="148" font-size="21" font-weight="500" text-anchor="middle">Psychological Safety</text>
</svg>

<!-- Content slide -->
<svg class="slide slide--content" viewBox="0 0 372 209" role="group" aria-label="Content slide">
  <rect width="372" height="209" fill="url(#photoDark)" role="img" aria-label="Dimmed photo: office desk with documents"/>
  <rect x="185" y="0" width="187" height="209" fill="var(--blue)"/>
  <circle cx="81" cy="45" r="3.5" fill="var(--blue)"/>
  <text class="t-white" x="93" y="49" font-size="9" font-weight="700" text-anchor="middle">MindHarbr</text>
  <text class="t-blue" x="93" y="54" font-size="3" text-anchor="middle">REALISING HUMAN POTENTIAL</text>
  <text class="t-blue" x="93" y="97" font-size="13" font-weight="500" text-anchor="middle">Slide Title</text>
  <text class="t-blue" x="93" y="112" font-size="13" font-weight="500" text-anchor="middle">Goes Here!</text>
  <g class="t-white" font-size="6.4" text-anchor="middle">
    <text x="93" y="135">Lorem ipsum dolor sit amet,</text>
    <text x="93" y="142.5">consectetur adipiscing elit. Vivamus</text>
    <text x="93" y="150">eu dui ex. Curabitur dapibus dignissim</text>
    <text x="93" y="157.5">dui, in molestie metus feugiat sed.</text>
  </g>
  <rect x="198" y="12" width="79" height="126" fill="#c9b8a4" role="img" aria-label="Photo: hands reviewing a printed document"/>
  <rect x="282" y="51" width="78" height="127" fill="#d8cdbc" role="img" aria-label="Photo: colleagues pointing at printed charts"/>
  <g class="t-ink" font-size="5.3" text-anchor="middle">
    <text x="320" y="19.5">Lorem ipsum dolor sit</text>
    <text x="320" y="25">amet, consectetur</text>
    <text x="320" y="30.5">adipiscing elit. Vivamus</text>
    <text x="320" y="36">eu dui ex. Curabitur</text>
    <text x="320" y="41.5">dapibus dignissim dui.</text>
    <text x="237" y="149">Lorem ipsum dolor sit</text>
    <text x="237" y="154.5">amet, consectetur</text>
    <text x="237" y="160">adipiscing elit. Vivamus</text>
    <text x="237" y="165.5">eu dui ex. Curabitur</text>
    <text x="237" y="171">dapibus dignissim dui.</text>
  </g>
  <rect x="0" y="201" width="372" height="8" fill="var(--ink)" opacity="0.35"/>
  <text x="25" y="206.3" font-size="3.6" class="t-white"><tspan font-weight="700">Lorn Ashby</tspan> © 2021 | www.<tspan font-weight="700">lornashby</tspan>.nz</text>
  <circle cx="357" cy="196" r="5" fill="var(--ink)"/>
  <text x="357" y="197.6" font-size="4.5" font-weight="700" text-anchor="middle" class="t-blue">4</text>
</svg>

<!-- Features slide -->
<svg class="slide slide--features" viewBox="0 0 372 209" role="group" aria-label="Features slide">
  <rect width="372" height="209" fill="url(#photoDark)" role="img" aria-label="Dimmed photo: meeting table with coffee cup"/>
  <circle cx="174" cy="45" r="4" fill="var(--blue)"/>
  <text class="t-white" x="186" y="49" font-size="11" font-weight="700" text-anchor="middle">MindHarbr</text>
  <text class="t-blue" x="186" y="55" font-size="3.6" text-anchor="middle">REALISING HUMAN POTENTIAL</text>
  <rect x="0" y="95" width="372" height="106" fill="var(--blue)" opacity="0.92"/>
  <g fill="none" stroke="var(--white)" stroke-width="1.4">
    <circle cx="61" cy="94" r="14" fill="var(--blue)"/>
    <circle cx="144" cy="94" r="14" fill="var(--blue)"/>
    <circle cx="227" cy="94" r="14" fill="var(--blue)"/>
    <circle cx="310" cy="94" r="14" fill="var(--blue)"/>
  </g>
  <g fill="var(--white)">
    <circle cx="61" cy="91" r="4.5"/>
    <rect x="58.5" y="95" width="5" height="4" rx="1"/>
    <circle cx="144" cy="94" r="6" fill="none" stroke="var(--white)" stroke-width="2.4" stroke-dasharray="2 1.4"/>
    <circle cx="144" cy="94" r="2.4" fill="none" stroke="var(--white)" stroke-width="1.2"/>
    <rect x="221" y="95" width="2.6" height="4"/>
    <rect x="225" y="92" width="2.6" height="7"/>
    <rect x="229" y="89" width="2.6" height="10"/>
  </g>
  <g fill="none" stroke="var(--white)" stroke-width="1.2">
    <circle cx="310" cy="94" r="6.5"/>
    <polyline points="310,90 310,94 313,94"/>
  </g>
  <g class="t-ink" text-anchor="middle">
    <g font-size="9.5" font-weight="500">
      <text x="61" y="120">Heading</text>
      <text x="144" y="120">Heading</text>
      <text x="227" y="120">Heading</text>
      <text x="310" y="120">Heading</text>
    </g>
    <g font-size="5.3">
      <text x="61" y="136">Lorem ipsum dolor sit</text><text x="61" y="141.7">amet, consectetur</text><text x="61" y="147.4">adipiscing elit. Vivamus</text><text x="61" y="153.1">eu dui ex. Curabitur</text><text x="61" y="158.8">dapibus dignissim dui, in</text><text x="61" y="164.5">molestie metus feugiat</text><text x="61" y="170.2">sed. Praesent aliquot.</text>
      <text x="144" y="136">Lorem ipsum dolor sit</text><text x="144" y="141.7">amet, consectetur</text><text x="144" y="147.4">adipiscing elit. Vivamus</text><text x="144" y="153.1">eu dui ex. Curabitur</text><text x="144" y="158.8">dapibus dignissim dui, in</text><text x="144" y="164.5">molestie metus feugiat</text><text x="144" y="170.2">sed. Praesent aliquot.</text>
      <text x="227" y="136">Lorem ipsum dolor sit</text><text x="227" y="141.7">amet, consectetur</text><text x="227" y="147.4">adipiscing elit. Vivamus</text><text x="227" y="153.1">eu dui ex. Curabitur</text><text x="227" y="158.8">dapibus dignissim dui, in</text><text x="227" y="164.5">molestie metus feugiat</text><text x="227" y="170.2">sed. Praesent aliquot.</text>
      <text x="310" y="136">Lorem ipsum dolor sit</text><text x="310" y="141.7">amet, consectetur</text><text x="310" y="147.4">adipiscing elit. Vivamus</text><text x="310" y="153.1">eu dui ex. Curabitur</text><text x="310" y="158.8">dapibus dignissim dui, in</text><text x="310" y="164.5">molestie metus feugiat</text><text x="310" y="170.2">sed. Praesent aliquot.</text>
    </g>
  </g>
  <rect x="0" y="201" width="372" height="8" fill="var(--navy)"/>
  <text x="25" y="206.3" font-size="3.6" class="t-white"><tspan font-weight="700">Lorn Ashby</tspan> © 2021 | www.<tspan font-weight="700">lornashby</tspan>.nz</text>
  <circle cx="357" cy="196" r="5" fill="var(--ink)"/>
  <text x="357" y="197.6" font-size="4.5" font-weight="700" text-anchor="middle" class="t-blue">5</text>
</svg>

<!-- Contact slide -->
<svg class="slide slide--contact" viewBox="0 0 372 209" role="group" aria-label="Contact slide">
  <rect width="372" height="209" fill="url(#photoDark)" role="img" aria-label="Dimmed photo: business handshake in an office"/>
  <circle cx="100" cy="80" r="4" fill="var(--blue)"/>
  <text class="t-white" x="41" y="84" font-size="11" font-weight="700">MindHarbr</text>
  <text class="t-blue" x="41" y="90" font-size="3.6">REALISING HUMAN POTENTIAL</text>
  <text class="t-white" x="42" y="126" font-size="9.5" font-weight="500">Contact Us</text>
  <g fill="none" stroke="var(--white)" stroke-width="0.8">
    <path d="M43.5 138.5 q0 5 4.5 6 l1 -1.4 -1.6 -1.2 -0.9 0.9 q-1.6 -0.8 -2 -2.4 l0.9 -0.8 -1 -1.6 z"/>
    <circle cx="46" cy="150.5" r="2.2"/>
    <circle cx="46" cy="161" r="3"/>
    <line x1="43" y1="161" x2="49" y2="161"/>
    <ellipse cx="46" cy="161" rx="1.3" ry="3"/>
  </g>
  <g class="t-white" font-size="5.5">
    <text x="54" y="143.5">2554-3810-4492</text>
    <text x="54" y="153.5">info@<tspan class="t-blue">lornashby</tspan>.nz</text>
    <text x="54" y="163.5">www.<tspan class="t-blue">lornashby</tspan>.nz</text>
  </g>
  <rect x="0" y="197" width="372" height="12" fill="var(--blue-deep)" opacity="0.55"/>
  <text x="155" y="205.3" font-size="3.6" class="t-white"><tspan font-weight="700">Lorn Ashby</tspan> © 2021 | www.<tspan font-weight="700">lornashby</tspan>.nz</text>
</svg>

</body>
</html>
```